Quillon Maison Wood Fired Pizza business card design

I have a logo and need an eye catching design that will get me noticed.
My business is wood fired pizza. I want a bold design that will make our customers remember us and the food that we serve. Work with the colors of our logo and texts. Maybe add designs that lend to what or how pizza is made using our wood fired oven?

Target Market(s)

Foodies!

Contact Information for Business Card

Quillon Maison Wood Fired Pizza
Our slogan is Fast. Fresh. Handcrafted
Catering for all events

Requirements
Must have
• Dana Porrick
Telephone 570 555 0183
website www.getquillon.example
Facebook @getquillonpizza maybe use the facebook logo next to it
Instagram getquillonpizza maybe use the instagram logo next to it
Catering for all events
Nice to have
• Maybe pizza peels, pizza cutters? Wood? Fired wood? Using our flame in the background?
Please work with different colored text so each sentence stands out? A themed color for facebook?
Maybe work with the colors within our logo?
Please try to use the our quillon font, but not a must have.

```html
<!DOCTYPE html>
<html lang="en">
<head>
<meta charset="utf-8">
<title>Quillon Maison Wood Fired Pizza – Business Cards</title>
<link href="https://fonts.googleapis.com/css2?family=Almendra:wght@700&family=Roboto+Condensed:wght@400;700&family=Nunito:wght@400&display=swap" rel="stylesheet">
<style>
  :root{
    --bg:#eceeed;
    --yellow:#fdc800;
    --yellow-deep:#f6b400;
    --red:#e01e26;
    --brown:#5f312f;
    --blush:#dcc3bd;
    --white:#ffffff;
    --orange:#f08a12;
    --ink:#2d2d2d;
    --crust:#d8a46a;
    --sauce:#e2582a;
  }
  *{box-sizing:border-box;margin:0;padding:0}
  html,body{width:1200px;height:837px;overflow:hidden;background:var(--bg)}
  .sheet{position:relative;width:1200px;height:837px}
  .card{position:absolute;width:431px;height:249px;border-radius:10px;overflow:hidden;box-shadow:0 6px 14px rgba(0,0,0,.18)}
  .card--front-gold{left:117px;top:150px;background:radial-gradient(circle at 18% 12%,var(--white) 0,var(--white) 14%,var(--yellow) 42%)}
  .card--front-white{left:628px;top:150px;background:var(--white)}
  .card--back-red{left:117px;top:442px;background:var(--yellow)}
  .card--back-brown{left:628px;top:442px;background:var(--white)}

  .brand{position:absolute;display:flex;align-items:center;gap:6px;font-family:"Roboto Condensed",sans-serif;font-weight:700;letter-spacing:1px;text-transform:uppercase;white-space:nowrap}
  .brand__dot{width:10px;height:10px;border-radius:50%}
  .brand--front{left:40px;top:78px;color:var(--red);font-size:17px}
  .brand--front .brand__dot{background:var(--red)}
  .brand--back{left:28px;top:100px;color:var(--white);font-size:19px}
  .brand--back .brand__dot{background:var(--white)}

  .holder{position:absolute;right:28px;top:58px;font-family:"Almendra",serif;font-weight:700;font-size:24px;color:var(--red);text-transform:uppercase;letter-spacing:.5px;white-space:nowrap}
  .slogan{position:absolute;left:30px;top:160px;font-family:"Roboto Condensed",sans-serif;font-weight:700;font-size:20px;color:var(--orange);white-space:nowrap}
  .slogan__sep{font-weight:400;margin:0 3px}
  .tagline{position:absolute;left:40px;top:186px;font-family:"Roboto Condensed",sans-serif;font-weight:400;font-size:21px;color:var(--ink);white-space:nowrap}
  .pizza{position:absolute;right:-40px;top:96px;width:180px;height:180px;border-radius:50%;background:radial-gradient(circle,var(--yellow-deep) 0,var(--sauce) 70%,var(--crust) 72%)}

  .wave{position:absolute;inset:0}
  .contact{position:absolute;left:246px;right:10px;top:134px;list-style:none;font-family:"Nunito",sans-serif;font-size:13.5px;color:var(--ink)}
  .contact li{display:flex;align-items:center;gap:7px;height:24px;white-space:nowrap}
  .contact svg{width:10px;height:10px;flex:none}
</style>
</head>
<body>
<main class="sheet">

  <section class="card card--front-gold">
    <div class="brand brand--front"><span class="brand__dot"></span>Quillon Maison</div>
    <h1 class="holder">Dana Porrick</h1>
    <p class="slogan">Fast<span class="slogan__sep">|</span>Fresh<span class="slogan__sep">|</span>Handcrafted</p>
    <p class="tagline">Catering for all events</p>
    <div class="pizza" role="img" aria-label="Sliced wood fired pizza illustration"></div>
  </section>

  <section class="card card--front-white">
    <div class="brand brand--front"><span class="brand__dot"></span>Quillon Maison</div>
    <h1 class="holder">Dana Porrick</h1>
    <p class="slogan">Fast<span class="slogan__sep">|</span>Fresh<span class="slogan__sep">|</span>Handcrafted</p>
    <p class="tagline">Catering for all events</p>
    <div class="pizza" role="img" aria-label="Sliced wood fired pizza illustration"></div>
  </section>

  <section class="card card--back-red">
    <svg class="wave" viewBox="0 0 431 249" preserveAspectRatio="none" aria-hidden="true">
      <path d="M0,0 H290 C292,120 150,150 80,249 H0 Z" fill="var(--white)" transform="translate(6,0)"/>
      <path d="M0,0 H290 C292,120 150,150 80,249 H0 Z" fill="var(--red)"/>
    </svg>
    <div class="brand brand--back"><span class="brand__dot"></span>Quillon Maison</div>
    <ul class="contact">
      <li><svg viewBox="0 0 10 10"><path d="M2 0.5 L3.8 2.6 L2.9 3.8 Q4 6 6.2 7.1 L7.4 6.2 L9.5 8 L8.3 9.5 Q3.5 9 0.5 1.7 Z" fill="var(--red)"/></svg>570 555 0183</li>
      <li><svg viewBox="0 0 10 10"><g fill="none" stroke="var(--red)" stroke-width="1"><circle cx="5" cy="5" r="4.3"/><ellipse cx="5" cy="5" rx="1.9" ry="4.3"/><path d="M0.7 5 H9.3 M1.5 3 H8.5 M1.5 7 H8.5"/></g></svg>www.getquillon.example</li>
      <li><svg viewBox="0 0 10 10"><circle cx="5" cy="5" r="4.5" fill="var(--red)"/></svg>@getquillonpizza</li>
      <li><svg viewBox="0 0 10 10"><rect x="0.5" y="0.5" width="9" height="9" rx="2" fill="var(--red)"/></svg>getquillonpizza</li>
    </ul>
  </section>

  <section class="card card--back-brown">
    <svg class="wave" viewBox="0 0 431 249" preserveAspectRatio="none" aria-hidden="true">
      <path d="M0,0 H290 C292,120 150,150 80,249 H0 Z" fill="var(--blush)" transform="translate(10,0)"/>
      <path d="M0,0 H290 C292,120 150,150 80,249 H0 Z" fill="var(--brown)"/>
    </svg>
    <div class="brand brand--back"><span class="brand__dot"></span>Quillon Maison</div>
    <ul class="contact">
      <li><svg viewBox="0 0 10 10"><path d="M2 0.5 L3.8 2.6 L2.9 3.8 Q4 6 6.2 7.1 L7.4 6.2 L9.5 8 L8.3 9.5 Q3.5 9 0.5 1.7 Z" fill="var(--red)"/></svg>570 555 0183</li>
      <li><svg viewBox="0 0 10 10"><g fill="none" stroke="var(--red)" stroke-width="1"><circle cx="5" cy="5" r="4.3"/><ellipse cx="5" cy="5" rx="1.9" ry="4.3"/><path d="M0.7 5 H9.3 M1.5 3 H8.5 M1.5 7 H8.5"/></g></svg>www.getquillon.example</li>
      <li><svg viewBox="0 0 10 10"><circle cx="5" cy="5" r="4.5" fill="var(--red)"/></svg>@getquillonpizza</li>
      <li><svg viewBox="0 0 10 10"><rect x="0.5" y="0.5" width="9" height="9" rx="2" fill="var(--red)"/></svg>getquillonpizza</li>
    </ul>
  </section>

</main>
</body>
</html>
```